Business Card Design/Stationary Design

We would like designers to submit cool, hip business card designs (plus stationary designs) for a new, upstart software development company located in Toronto.
If you have any questions, please email us.
For inspiration on designs:
http://cardmuse.example/cool-business-cards/
http://layoutnotes.example/2008/05/36-cool-business-cards-you-should%E2%80%99ve-seen.html
http://gigharbor.example/general/18-smokin-hot-business-card-designs/

Card info:

Selvakumar (Selv) Nadarasan

Founder and CEO

47 Brindle Court, Suite 311

Toronto, ON M4K 2T8

Phone: 647-512-7730

Mobile: 416-273-5094

Fax: 647-512-7731

Email: selvakumar.nadarasan@mailbrook.example

www.quendrix.example
Updates

Hi everyone,

In terms of all the designs I have seen so far, here is what I like:

1.  I really like the "back" part of this design.  The "front" looks pretty decent as well, but for the "front", look at #2 on this list.  I like that.

http://www.pitchboard.example/image.aspx?imageLocation=1000_10001_2000_image.jpg&type=design300px&whiteLabelCustId=9999

2. "Side 1" of this I like, the front needs to be reworked.

http://www.pitchboard.example/image.aspx?imageLocation=1000_10002_2000_image.png&type=design300px&whiteLabelCustId=9999

3. http://www.pitchboard.example/image.aspx?imageLocation=1000_10003_2000_image.jpg&type=design300px&whiteLabelCustId=9999

4. http://www.pitchboard.example/image.aspx?imageLocation=1000_10004_2000_image.jpg&type=design300px&whiteLabelCustId=9999

Target Market(s)

We are focused on enterprise customers right now, so businesses with a long-term goal of also reaching out to the consumer market as well.

Industry/Entity Type

Software

Requirements
Must have
• Must look cool, ultra-modern, clean and eye-catching. Must incorporate our logo and the colors found in the logo.

```html
<!DOCTYPE html>
<html lang="en">
<head>
<meta charset="utf-8">
<title>Quendrix Technologies – Business Card</title>
<link rel="stylesheet" href="https://fonts.googleapis.com/css2?family=Questrial&display=swap">
<style>
  :root {
    --lime: #adc443;
    --olive: #5e6346;
    --olive-soft: #6b6f55;
    --paper: #ffffff;
    --ink-light: #f4f7de;
    --backdrop: #e9e7e2;
  }
  * { box-sizing: border-box; margin: 0; padding: 0; }
  html, body { width: 1200px; height: 900px; overflow: hidden; }
  body {
    background: var(--backdrop);
    font-family: "Questrial", "Century Gothic", sans-serif;
    position: relative;
  }
  .card {
    position: absolute;
    left: 250px;
    width: 700px;
    height: 400px;
    overflow: hidden;
  }

  /* Front side */
  .card-front {
    top: 30px;
    background: var(--lime);
    border-top-right-radius: 56px;
  }
  .front-brand {
    position: absolute;
    left: 0;
    top: 320px;
    height: 76px;
    padding-left: 32px;
    border-left: 7px solid var(--olive);
    color: var(--olive);
  }
  .front-brand .brand-name {
    font-size: 46px;
    line-height: 1;
    display: block;
    padding-top: 6px;
  }
  .front-brand .brand-tagline {
    display: block;
    text-align: right;
    font-size: 10px;
    letter-spacing: 0.5px;
    margin-top: 2px;
  }

  /* Back side */
  .card-back {
    top: 460px;
    background: var(--lime);
    border-top-left-radius: 56px;
  }
  .back-header {
    position: absolute;
    left: 0; top: 0;
    width: 100%;
    height: 164px;
    background: var(--paper);
  }
  .back-brand {
    position: absolute;
    left: 30px;
    top: 46px;
    display: flex;
    align-items: center;
    color: var(--olive);
  }
  .brand-dot {
    width: 70px;
    height: 70px;
    border-radius: 50%;
    background: var(--lime);
    margin-right: 14px;
  }
  .back-brand .brand-name {
    font-size: 46px;
    line-height: 1;
    display: block;
  }
  .back-brand .brand-tagline {
    display: block;
    text-align: right;
    font-size: 10px;
    letter-spacing: 0.5px;
    margin-top: 2px;
  }
  .person {
    position: absolute;
    right: 42px;
    top: 64px;
    text-align: right;
    color: var(--olive-soft);
  }
  .person-name { font-size: 17px; }
  .person-title {
    font-size: 18px;
    letter-spacing: 1.5px;
    color: var(--olive);
    font-weight: 700;
    margin-top: 2px;
  }
  .contact-list {
    position: absolute;
    left: 128px;
    top: 180px;
    list-style: none;
    color: var(--ink-light);
    font-size: 16px;
  }
  .contact-list li {
    display: flex;
    height: 27.6px;
    align-items: center;
  }
  .contact-label {
    width: 42px;
    color: var(--olive-soft);
  }
  .back-footer {
    position: absolute;
    left: 0; bottom: 0;
    width: 100%;
    height: 34px;
    background: var(--olive);
  }
</style>
</head>
<body>
  <section class="card card-front" aria-label="Card front">
    <div class="front-brand">
      <span class="brand-name">Quendrix</span>
      <span class="brand-tagline">TECHNOLOGIES INC.</span>
    </div>
  </section>

  <section class="card card-back" aria-label="Card back">
    <header class="back-header">
      <div class="back-brand">
        <span class="brand-dot"></span>
        <div>
          <span class="brand-name">Quendrix</span>
          <span class="brand-tagline">TECHNOLOGIES INC.</span>
        </div>
      </div>
      <div class="person">
        <p class="person-name">Selvakumar (Selv) Nadarasan</p>
        <p class="person-title">FOUNDER AND CEO</p>
      </div>
    </header>
    <ul class="contact-list">
      <li><span class="contact-label">p:</span><span>647.512.7730</span></li>
      <li><span class="contact-label">m:</span><span>416.273.5094</span></li>
      <li><span class="contact-label">f:</span><span>647.512.7731</span></li>
      <li><span class="contact-label">w:</span><span>www.quendrix.example</span></li>
      <li><span class="contact-label">e:</span><span>selvakumar.nadarasan@mailbrook.example</span></li>
      <li><span class="contact-label">a:</span><span>47 Brindle Court, Suite 311, Toronto, ON M4K 2T8</span></li>
    </ul>
    <footer class="back-footer"></footer>
  </section>
</body>
</html>
```